Influencer for sustainable living needs Youtube banner.

We are launching a Youtube Channel called "Reachable Greenhearth With Dorian Palk" and need a Youtube design banner that will represent the channel's theme, branding, and content. The size of the banner must be 2560 x 1440 pixels with an optimized area of 1546 x 423 pixels that views well on all device types.

The banner needs to have the title of the channel, the subline of the types of content (Tours | DIY Guides | Inspiration), and display Dorian Palk or his face. I have attached a picture of Dorian. We are open to using it as is or stylized.

The 3 types of Pillar content on the channel are:
1) Tours of sustainable properties and homes.
2) DIY educational and instructional videos.
3) Inspirational talks and interviews on sustainability and Permaculture.

The main purpose of the channel is to build our larger audience, increase trust and authority, and direct traffic to our paid educational offerings. Our paid educational offerings are hosted at “ReachableGreenhearthSchool.example”. Click through the website to better understand our branding & offerings. (Brand Manual and logo also attached)

The "influencer" is the founder of the School - Dorian Palk. He is a passionate, charismatic, and cheerful personality, who believes in the potential of humanity to create landscapes that thrive, so we can thrive within them. His core message is that humans can prove they are not a parasite by getting their homes, gardens, and communities in order so they shelter and feed us.

Files attached include versions of our logo and a branding manual for the School (note: the branding manual does not need to be followed exactly as it for the School (ReachableGreenhearthSchool.example) and not the Youtube channel (Reachable Greenhearth With Dorian Palk)... but the youtube channel branding should be similar.

DIYers, home owners, property owners, sustainable minded people, gardeners, homesteaders

Education, Sustainable living, Permaculture, Lifestyle

• Roboto & Urbanist. See design manual.

• Clean and bright design. Not cliche. Use of colours, fonts, and more from brand manual.
• I would like to see banner which compares to other professional youtubers.

```html
<!DOCTYPE html>
<html lang="en">
<head>
<meta charset="utf-8">
<title>Reachable Greenhearth – Channel Banner</title>
<link href="https://fonts.googleapis.com/css2?family=Urbanist:wght@600;700;800&family=Roboto:wght@400;500;700&display=swap" rel="stylesheet">
<style>
  :root {
    --page-bg: #eceeef;
    --deep-teal: #0f4259;
    --mid-teal: #1d7a82;
    --bright-teal: #2fb3a6;
    --lime: #a6d13d;
    --navy: #0f3a5f;
    --white: #ffffff;
  }
  * { margin: 0; padding: 0; box-sizing: border-box; }
  html, body { width: 1001px; height: 1200px; overflow: hidden; background: var(--page-bg); }
  .banner {
    position: absolute; left: 0; top: 318px;
    width: 1001px; height: 563px; overflow: hidden;
    background: var(--deep-teal);
  }
  .banner-art { position: absolute; inset: 0; }
  .host-photo {
    position: absolute; left: 277px; top: 200px; width: 163px; height: 171px;
    background: linear-gradient(180deg, #8a6c5a 0%, #c49a84 35%, #1f2d55 62%, #16234a 100%);
    border-radius: 70px 70px 0 0;
  }
  .title-block {
    position: absolute; left: 440px; top: 218px; width: 270px;
    text-align: center; font-family: "Urbanist", sans-serif; color: var(--white);
  }
  .channel-title {
    font-weight: 700; font-size: 42px; line-height: 37px; letter-spacing: -0.5px;
  }
  .channel-host {
    display: inline-block; margin-top: 4px; padding: 0 4px 2px;
    font-family: "Roboto", sans-serif; font-weight: 500; font-size: 25px; line-height: 28px;
    color: var(--navy); border-bottom: 2px solid var(--navy);
  }
  .content-pillars {
    margin-top: 6px; font-family: "Roboto", sans-serif; font-weight: 500;
    font-size: 12.5px; color: var(--white);
  }
  .school-mark {
    position: absolute; left: 719px; top: 216px;
    display: flex; align-items: center; gap: 5px;
  }
  .school-dot { width: 20px; height: 20px; border-radius: 50%; background: var(--white); opacity: 0.85; }
  .school-name {
    font-family: "Urbanist", sans-serif; font-weight: 600; font-size: 8px; line-height: 9px;
    color: var(--white);
  }
</style>
</head>
<body>
  <section class="banner">
    <svg class="banner-art" width="1001" height="563" viewBox="0 0 1001 563" aria-hidden="true">
      <defs>
        <linearGradient id="lightBand" x1="0" y1="0" x2="1" y2="1">
          <stop offset="0" stop-color="#2aa59c"/>
          <stop offset="0.55" stop-color="#2a9e8c"/>
          <stop offset="1" stop-color="#9ccc42"/>
        </linearGradient>
        <linearGradient id="lowerBand" x1="0" y1="0" x2="1" y2="0">
          <stop offset="0" stop-color="#1a6a70"/>
          <stop offset="1" stop-color="#3db8a6"/>
        </linearGradient>
        <linearGradient id="centerStrip" x1="0" y1="0" x2="1" y2="0">
          <stop offset="0" stop-color="#1a6e7e"/>
          <stop offset="0.4" stop-color="#2fb0a2"/>
          <stop offset="0.7" stop-color="#7fc64c"/>
          <stop offset="0.85" stop-color="#1d6c7a"/>
          <stop offset="1" stop-color="#13506a"/>
        </linearGradient>
      </defs>
      <rect width="1001" height="563" fill="var(--deep-teal)"/>
      <polygon points="0,0 215,0 0,125" fill="#1e8c92"/>
      <polygon points="215,0 330,0 1001,370 1001,470" fill="url(#lightBand)"/>
      <polygon points="0,125 215,0 1001,470 1001,563 905,563" fill="#174f66" opacity="0.6"/>
      <polygon points="230,370 1001,370 1001,563 905,563" fill="url(#lowerBand)" opacity="0.55"/>
      <polygon points="1001,380 1001,563 910,563" fill="#3cc0b0" opacity="0.7"/>
      <rect y="204" width="1001" height="166" fill="url(#centerStrip)"/>
      <rect y="204" width="290" height="166" fill="#2c6670" opacity="0.7" role="img" aria-label="Photo of a sustainable home with a garden"/>
    </svg>
    <div class="host-photo" role="img" aria-label="Portrait of Dorian Palk smiling, wearing a navy jacket"></div>
    <div class="title-block">
      <h1 class="channel-title">Reachable<br>Greenhearth</h1>
      <p class="channel-host">With Dorian Palk</p>
      <p class="content-pillars">Tours | DIY Guides | Inspiration</p>
    </div>
    <div class="school-mark">
      <span class="school-dot"></span>
      <span class="school-name">Reachable<br>Greenhearth School</span>
    </div>
  </section>
</body>
</html>
```